Monthly Parking offer

Brief details: -
About the company: Harbourline Parking is a Car Parking company with car parks all over the world.

Flyer details: Looking to create an A5 flyer to promote monthly parking to new customers

What flyer should READ:

Park for free!

"monthly parking from $10 a day"
park for free until 30th of June 2014
Contact (03) 8472 519
www.harbourlineparking.com.au

Parking

Colors
fbee3f
34a6d7
f04a50

```html
<!DOCTYPE html>
<html lang="en">
<head>
<meta charset="utf-8">
<title>Harbourline Parking – Monthly Parking Flyer</title>
<link rel="stylesheet" href="https://fonts.googleapis.com/css2?family=Oswald:wght@400;500;600&family=Roboto+Condensed:ital,wght@0,400;0,700;1,400&display=swap">
<style>
  :root {
    --stage: #e9e9e9;
    --yellow: #fbee3f;
    --yellow-deep: #f7d92a;
    --blue: #34a6d7;
    --blue-deep: #1d8fc4;
    --red: #f04a50;
    --pink: #e8445a;
    --band-red: #e31b2e;
    --band-dark: #3a3a3c;
    --orange: #f9b233;
    --gold: #f2b01e;
    --ink: #111111;
    --white: #ffffff;
  }
  * { box-sizing: border-box; margin: 0; padding: 0; }
  html, body { width: 1200px; height: 1000px; overflow: hidden; }
  body { background: var(--stage); font-family: "Roboto Condensed", sans-serif; position: relative; }

  .flyer {
    position: absolute; left: 246px; top: 0; width: 708px; height: 1000px;
    overflow: hidden; background: var(--yellow);
  }
  .flyer__pattern {
    position: absolute; inset: 0 0 180px 0;
    background: radial-gradient(ellipse at 50% 40%, var(--yellow) 0%, var(--yellow-deep) 100%);
  }

  .badge {
    position: absolute; left: 172px; top: 88px; width: 362px; height: 400px;
    border-radius: 34px; background: #d7dadd; padding: 9px;
    box-shadow: 0 3px 8px rgba(0,0,0,.25);
  }
  .badge__inner {
    width: 100%; height: 100%; border-radius: 28px;
    background: radial-gradient(circle at 50% 40%, var(--blue) 0%, var(--blue-deep) 100%);
    display: flex; flex-direction: column; justify-content: center; align-items: center;
  }
  .badge__line {
    font-family: "Oswald", sans-serif; font-weight: 500; color: var(--white);
    font-size: 104px; line-height: 104px; letter-spacing: 1px;
  }

  .offer {
    position: absolute; left: 0; width: 100%;
    font-family: "Oswald", sans-serif; font-weight: 600; color: var(--pink);
    top: 530px; font-size: 38px; line-height: 60px;
    display: flex; justify-content: center; align-items: center; gap: 6px;
  }
  .offer__coin {
    width: 80px; height: 80px; border-radius: 50%;
    background: radial-gradient(circle at 40% 35%, #ffe27a, var(--gold) 70%, #d38c10);
    display: inline-flex; align-items: center; justify-content: center;
    font-size: 36px; color: var(--red);
  }

  .until {
    position: absolute; top: 623px; left: 0; width: 100%; text-align: center;
    color: var(--pink); font-size: 30px; font-weight: 700; letter-spacing: .5px;
  }
  .until em { font-style: italic; font-weight: 400; }

  .contact { position: absolute; top: 683px; left: 0; width: 100%; text-align: center; color: var(--ink); }
  .contact__lead { font-size: 18px; }
  .contact__phone { font-weight: 700; font-size: 28px; margin-top: 10px; }
  .contact__rule { width: 332px; height: 2px; background: var(--ink); margin: 4px auto 6px; }
  .contact__web { font-weight: 700; font-size: 28px; }

  .rewards { position: absolute; top: 832px; left: 0; width: 100%; height: 50px; display: flex; }
  .rewards__name {
    width: 206px; background: var(--band-dark); color: var(--white);
    font-size: 14px; letter-spacing: 4px; display: flex; align-items: center; justify-content: center;
  }
  .rewards__text {
    flex: 1; background: var(--band-red); color: var(--white); font-weight: 700;
    font-size: 14px; line-height: 17px; padding: 8px 0 0 24px;
  }

  .footer { position: absolute; top: 882px; left: 0; width: 100%; height: 118px; background: var(--orange); }
  .footer__plan {
    position: absolute; left: 0; width: 100%; top: 12px; text-align: center;
    font-weight: 700; font-size: 14px; line-height: 18px; color: var(--ink);
  }
  .footer__follow { display: flex; justify-content: center; align-items: center; gap: 6px; margin-top: 6px; }
  .footer__follow span { display: inline-block; width: 16px; height: 16px; background: var(--blue-deep); }
  .footer__terms { position: absolute; left: 40px; bottom: 40px; font-size: 10px; color: #333; }
  .brand { position: absolute; right: 36px; top: 16px; text-align: center; width: 120px; }
  .brand__row { display: flex; align-items: center; gap: 6px; justify-content: center; }
  .brand__mark { width: 28px; height: 28px; background: var(--blue-deep); }
  .brand__name { font-weight: 700; font-size: 14px; line-height: 15px; color: var(--blue-deep); text-align: left; }
  .brand__tag { font-size: 11px; color: var(--ink); margin-top: 4px; }
</style>
</head>
<body>
  <article class="flyer">
    <div class="flyer__pattern" role="img" aria-label="Yellow grid pattern of parking bays"></div>

    <div class="badge">
      <div class="badge__inner">
        <div class="badge__line">PARK</div>
        <div class="badge__line">FOR</div>
        <div class="badge__line">FREE!</div>
      </div>
    </div>

    <div class="offer">monthly parking from <span class="offer__coin">$10</span> a day</div>

    <div class="until">Park For Free until <em>30th of June 2014</em></div>

    <div class="contact">
      <div class="contact__lead">for more information feel free to contact us :</div>
      <div class="contact__phone">Phone (03) 8472 519</div>
      <div class="contact__rule"></div>
      <div class="contact__web">www.harbourlineparking.com.au</div>
    </div>

    <div class="rewards">
      <div class="rewards__name">SKYWAY REWARDS</div>
      <div class="rewards__text">Earn up to 20,000 Skyway Points when you sign up for Monthly Parking<br>at selected Car Parks*</div>
    </div>

    <footer class="footer">
      <div class="footer__plan">
        Plan before you Park<br>www.harbourlineparking.com.au
        <div class="footer__follow">Follow us <span></span><span></span></div>
      </div>
      <div class="footer__terms">*Conditions apply. Visit harbourlineparking.com.au/srw</div>
      <div class="brand">
        <div class="brand__row">
          <div class="brand__mark"></div>
          <div class="brand__name">Harbourline<br>Parking</div>
        </div>
        <div class="brand__tag">Park With Ease</div>
      </div>
    </footer>
  </article>
</body>
</html>
```